TRV Flyer

We need a professional design for flyers that we produce. The attached event draft is typical of the majority of flyers we will produce, and is the one that we need to do right now.

We would also like the source files for the design. We don’t have Corel Draw, but can work with any files produced in Adobe Creative Suite products.

Target Market(s)

Owners of residential apartments

Industry/Entity Type

Non-Profit

Requirements
Must have
• Design must be complimentary to our new website design at www.trv.org.au so we can establish consistent branding.
• Any fonts used must be freely avalaible standard fonts used in Microsoft Word

```html
<!DOCTYPE html>
<html lang="en">
<head>
<meta charset="utf-8">
<title>TRV Educational Workshop Flyer</title>
<link rel="stylesheet" href="https://fonts.googleapis.com/css2?family=Questrial&family=Montserrat:wght@800&family=Arimo:ital,wght@0,400;1,400&family=Roboto+Condensed:wght@400&display=swap">
<style>
  :root {
    --navy: #1f3872;
    --blue: #2d4a8c;
    --gold: #d59a2d;
    --gold-dark: #b8892f;
    --gold-pale: #ebc98e;
    --slate: #7d83ac;
    --ink: #1a1a1a;
    --white: #ffffff;
  }
  * { margin: 0; padding: 0; box-sizing: border-box; }
  html, body { width: 848px; height: 1200px; overflow: hidden; background: var(--white); }
  .flyer { position: relative; width: 848px; height: 1200px; overflow: hidden; font-family: "Arimo", Arial, sans-serif; color: var(--ink); }
  .backdrop { position: absolute; inset: 0; }

  .brand { position: absolute; left: 44px; top: 30px; display: flex; align-items: center; gap: 10px; }
  .brand-mark { width: 16px; height: 16px; background: var(--gold); }
  .brand-name { font-family: "Questrial", sans-serif; color: var(--blue); font-size: 19px; line-height: 17px; letter-spacing: 1.5px; text-transform: uppercase; }

  .badge { position: absolute; left: 21px; top: 134px; font-family: "Questrial", sans-serif; color: var(--white); font-size: 23px; line-height: 28px; }

  .headline { position: absolute; right: 38px; top: 22px; text-align: right; font-family: "Questrial", sans-serif; color: var(--white); }
  .headline .lead { font-size: 31px; line-height: 34px; letter-spacing: 0.5px; }
  .headline .strong { font-family: "Montserrat", sans-serif; font-weight: 800; color: var(--gold); font-size: 30px; line-height: 36px; letter-spacing: 1px; margin-top: 2px; }
  .headline .dates { font-size: 31px; line-height: 40px; margin-top: 0; }
  .register { position: absolute; right: 38px; top: 216px; text-align: right; font-family: "Montserrat", sans-serif; font-weight: 800; color: var(--white); font-size: 21px; line-height: 28px; letter-spacing: 1px; }

  .intro { position: absolute; left: 104px; top: 313px; width: 470px; font-size: 16.5px; line-height: 20.5px; }
  .intro ul { list-style: none; margin: 4px 0; }
  .intro li { position: relative; padding-left: 13px; margin: 4px 0; }
  .intro li::before { content: "•"; position: absolute; left: 0; }

  .details { position: absolute; left: 104px; top: 497px; font-size: 16.5px; line-height: 24.5px; color: var(--gold); }
  .details .row { display: flex; }
  .details .label { width: 77px; }
  .details .note { color: var(--ink); }

  .programme-title { position: absolute; left: 104px; top: 644px; font-family: "Questrial", sans-serif; color: var(--gold); font-size: 22px; letter-spacing: 1px; }
  .programme-text { position: absolute; left: 104px; top: 670px; width: 660px; font-size: 16.5px; line-height: 20.5px; }
  .programme-text p + p { margin-top: 4px; }

  .sessions { position: absolute; left: 26px; top: 760px; font-family: "Roboto Condensed", sans-serif; color: var(--white); font-size: 17px; }
  .sessions .row { display: flex; height: 25px; margin-bottom: 4px; }
  .sessions .cell { height: 25px; line-height: 25px; padding-left: 8px; }
  .sessions .period { width: 76px; margin-right: 3px; background: var(--gold); }
  .sessions .period.blank { background: transparent; }
  .sessions .topic { width: 119px; margin-right: 4px; background: var(--slate); }
  .sessions .speaker { width: 547px; background: var(--navy); }
  .sessions .head .topic { background: var(--gold-pale); }
  .sessions .head .speaker { background: var(--gold); }

  .theme-title { position: absolute; left: 101px; top: 895px; font-family: "Questrial", sans-serif; color: var(--gold); font-size: 22px; letter-spacing: 1px; }
  .theme-story { position: absolute; left: 101px; top: 928px; width: 676px; font-style: italic; font-size: 16.2px; line-height: 20.6px; }

  .footer { position: absolute; left: 0; top: 1133px; width: 848px; height: 67px; background: linear-gradient(90deg, #2a64ad, #233f86); color: var(--white); font-family: "Questrial", sans-serif; font-size: 15px; line-height: 19px; text-align: center; padding-top: 13px; letter-spacing: 0.3px; }
</style>
</head>
<body>
<div class="flyer">
  <svg class="backdrop" width="848" height="1200" viewBox="0 0 848 1200">
    <defs>
      <linearGradient id="skyline" x1="0" y1="0" x2="1" y2="1">
        <stop offset="0" stop-color="#2c4a8c"/>
        <stop offset="0.55" stop-color="#3d4f8d"/>
        <stop offset="1" stop-color="#5a5a90"/>
      </linearGradient>
      <linearGradient id="goldfade" x1="0" y1="0" x2="1" y2="0">
        <stop offset="0" stop-color="#b8892f"/>
        <stop offset="1" stop-color="#d6a038"/>
      </linearGradient>
    </defs>
    <polygon points="0,76 219,165 0,437" fill="url(#goldfade)"/>
    <polygon points="351,0 848,0 848,420 219,165" fill="url(#skyline)" role="img" aria-label="Photograph of a modern apartment building tinted in blue"/>
  </svg>

  <div class="brand">
    <span class="brand-mark"></span>
    <div class="brand-name">Titleholders<br>Residential<br>Voice</div>
  </div>

  <div class="badge">TRV<br>Educational<br>Workshop</div>

  <div class="headline">
    <div class="lead">“The Essentials<br>of Strata Living –</div>
    <div class="strong">What Every Owner<br>Needs to Know”</div>
    <div class="dates">12th and 26th June 2010</div>
  </div>
  <div class="register">Register at<br>www.trv.org.au</div>

  <div class="intro">
    <p>This workshop is for owners in strata apartments who want to learn more about</p>
    <ul>
      <li>getting the best out of apartment living</li>
      <li>protecting their home and their investment</li>
    </ul>
    <p>AND particularly for</p>
    <ul>
      <li>executive committee members to know their rights and responsibilities in managing their strata scheme</li>
    </ul>
  </div>

  <div class="details">
    <div class="row"><span class="label">Location:</span><span>Harbourside Club<br>24 Wattle Parade, Bayview Point 2061</span></div>
    <div class="row"><span class="label">Dates:</span><span>The workshop will run twice – on 12th June and 26th June 2010</span></div>
    <div class="row"><span class="label">Time:</span><span>10.00 am to 4.00 pm.</span></div>
    <div class="row"><span class="label">Cost:</span><span>$60.00, which includes morning tea and lunch.</span></div>
    <div class="note">The maximum number of participants for each workshop is 60.</div>
  </div>

  <div class="programme-title">Programme:</div>
  <div class="programme-text">
    <p>The day will comprise four sessions, each facilitated by a specialist.</p>
    <p>In each session the speaker will provide relevant information and set the topics for group work; participants will break into groups and work up solutions to each topic; and the groups will compare outcomes.</p>
  </div>

  <div class="sessions">
    <div class="row head"><div class="cell period blank"></div><div class="cell topic">Topic</div><div class="cell speaker">Speaker</div></div>
    <div class="row"><div class="cell period">Morning</div><div class="cell topic">Governance</div><div class="cell speaker">Martin Hale, strata lawyer</div></div>
    <div class="row"><div class="cell period blank"></div><div class="cell topic">Management</div><div class="cell speaker">Peter Linford, seasoned former chairperson and executive committee member</div></div>
    <div class="row"><div class="cell period">Afternoon</div><div class="cell topic">Financials</div><div class="cell speaker">David Ashcroft, accountant</div></div>
  </div>

  <div class="theme-title">The day’s theme will be:</div>
  <p class="theme-story">Gina is a new owner in her building called Utopia Tower. She notices some management processes which to her seem strange. She is elected to the executive committee and finds that the developer has retained more control than she realised - the service providers have long-term and onerous contracts, and she doesn’t seem to be able to exert enough influence. What does the law require her to do, as a committee member? How does she influence good management processes? The finances seem to be out of control, so how can she fix them so she doesn’t pay inflated levies each year and lose value on her investment? ... and then the neighbour above her apartment installs a timber floor and she has noise problems ... and the building seems to have a lot of defects .............</p>

  <div class="footer">Enroll Now - Learn A Lot - Have Some Fun As Well - Share Experiences -<br>Find Out How TRV Can Help You In The Longer Term.</div>
</div>
</body>
</html>
```